Design Memorial Booklet for our Mum

We have put together 4,400 words with 57 photos of our mum who passed away recently. Due to covid restrictions, we were unable to hold a funeral with all the family and friends so we planning to send an A5 booklet out to them to celebrate her life instead.
The booklet should be beautiful and celebrate her life focussing on the vibrant photos of her.
All text and low resolution photos are in this document: Quillo https://pages.quillo-example.net/doc/7kRw2pLmNx94TqzVbHs0cJe5YuA3dFgKiO8nW1rXtb/edit?share=link

Photos: https://store.quillo-example.net/box/folders/9pLqWx4eR7tYu2Io8aS-dFgH3jK6lZ?share=link

We can give access to a folder with high resolution photos for the final print file.
Booklet will be printed in A5 (A4 folded in half and bound) so final format will need to be in page multiples of 4.

Output file type: pdf - ready for printing + raw file (InDesign or similar)

Update: For this competition please can you submit the cover page plus 1-2 inside pages to show us the style. Based on this we will select a winner to complete the work.

We are looking for a fast turnaround on this project.

Thanks for your patience for us new users of this.

Target Market(s)

Friends and Family

Industry/Entity Type

Personal Project

Requirements
Must have
• Look professional. Let the beautiful photos be the feature. Creative but respectful.

```html
<!DOCTYPE html>
<html lang="en">
<head>
<meta charset="utf-8">
<title>Elena Harrow – Memorial Booklet</title>
<link rel="stylesheet" href="https://fonts.googleapis.com/css2?family=Source+Sans+3:wght@400;600;700&family=Alex+Brush&family=Montserrat:wght@400;700&display=swap">
<style>
  :root{
    --stage:#1f1f21;
    --paper:#ffffff;
    --paper-shade:#f1f1f1;
    --pink:#d6246e;
    --pink-light:#ec6aa0;
    --pink-deep:#b3175a;
    --charcoal:#2c2c2e;
    --band:#3b3b3d;
    --ink:#3a3a3a;
    --ink-soft:#666;
  }
  *{box-sizing:border-box;margin:0;padding:0}
  html,body{width:1200px;height:3840px;overflow:hidden;background:var(--stage)}
  body{position:relative;font-family:"Source Sans 3",Arial,sans-serif;color:var(--ink)}
  .page,.spread{position:absolute;background:var(--paper);overflow:hidden;box-shadow:0 14px 40px rgba(0,0,0,.5)}
  .spread{width:1100px;height:778px;left:50px;display:flex}
  .spread-page{position:relative;width:550px;height:778px;overflow:hidden}
  .spread-page.left{background:linear-gradient(90deg,var(--paper) 85%,var(--paper-shade))}
  .spread-page.right{background:linear-gradient(90deg,var(--paper-shade),var(--paper) 12%)}
  .photo{position:absolute}
  .script{font-family:"Alex Brush",cursive;font-weight:400}

  /* Cover */
  .cover{left:330px;top:70px;width:540px;height:764px}
  .cover-tab{position:absolute;top:0;right:95px;width:170px;height:68px;background:var(--pink-light)}
  .cover-title{position:absolute;top:108px;left:58px;right:40px;font-weight:700;font-size:40px;line-height:38px;color:var(--pink);text-align:right}
  .cover-title span{display:block}
  .cover-bar{position:absolute;top:245px;right:80px;width:135px;height:330px;background:linear-gradient(180deg,var(--pink-light),var(--pink-deep));z-index:2}
  .cover-nickname{position:absolute;top:250px;left:120px;font-size:62px;color:var(--charcoal);z-index:3}
  .cover-tagline{position:absolute;top:335px;left:118px;font-family:Montserrat,sans-serif;font-size:15px;letter-spacing:5px;color:var(--ink);z-index:3}
  .cover-photo{left:140px;top:380px;right:0;bottom:0;background:linear-gradient(160deg,#5f8a4a,#7ea25a 40%,#e98a7a 70%,#3a3338);z-index:1}

  /* Contents */
  .contents-head{position:absolute;top:150px;left:60px;font-weight:700;font-size:50px;letter-spacing:1px;color:var(--pink)}
  .contents-rule{position:absolute;top:200px;left:50px}
  .contents-list{position:absolute;top:240px;left:180px;width:300px;list-style:none;font-size:13px;color:var(--ink-soft)}
  .contents-list li{display:flex;justify-content:space-between;margin-bottom:6px}
  .contents-list li.gap{margin-top:18px}
  .contents-list .sub{padding-left:18px}
  .poem-page{background:linear-gradient(180deg,var(--pink-light),var(--pink) 70%,var(--pink-deep))!important}
  .poem{position:absolute;top:60px;left:90px;right:90px;text-align:center;color:#fff;font-size:12px;line-height:15px}
  .poem p{margin-bottom:14px}
  .poem-wave{position:absolute;left:0;bottom:0}

  /* Celebration spread */
  .celebration-band{position:absolute;top:90px;left:0;width:1100px;height:96px}
  .celebration-title{position:absolute;top:100px;left:60px;color:#fff;font-weight:700;font-size:36px;display:flex;align-items:baseline;gap:12px}
  .celebration-title .script{font-size:52px}
  .section-head{position:absolute;font-size:27px;color:var(--pink)}
  .body-copy{position:absolute;font-size:12.5px;line-height:15.5px;color:var(--ink)}
  .body-copy p{margin-bottom:12px}
  .body-copy p::first-letter{font-size:30px;float:left;line-height:26px;margin-right:3px}
  .photo-band{position:absolute;left:0;right:0;top:470px;height:255px;background:var(--charcoal)}
  .band-line{position:absolute;left:0;right:0;height:5px;background:var(--pink)}

  /* Memories spread */
  .dark-page{background:var(--charcoal)!important}
  .dark-page .body-copy{color:#eee}
</style>
</head>
<body>

<!-- Cover -->
<section class="page cover">
  <div class="cover-tab"></div>
  <h1 class="cover-title"><span>ELENA MARISOL</span><span>TERESA HARROW</span><span>(née Pereira)</span></h1>
  <div class="cover-bar"></div>
  <div class="cover-nickname script">Nana Wren</div>
  <div class="cover-tagline">EXTRAORDINAIRE</div>
  <div class="photo cover-photo" role="img" aria-label="Photo of Elena smiling among rose bushes, holding a peach rose"></div>
</section>

<!-- Contents and poem -->
<section class="spread" style="top:920px">
  <div class="spread-page left">
    <h2 class="contents-head">CONTENT</h2>
    <svg class="contents-rule" width="460" height="30" viewBox="0 0 460 30"><path d="M0 24 Q230 4 460 10" stroke="var(--pink)" stroke-width="4" fill="none"/></svg>
    <ul class="contents-list">
      <li><span>Poem to Elena</span><span>01</span></li>
      <li class="gap"><span>A Celebration of Nana Wren's Life</span><span></span></li>
      <li><span class="sub">Parent to Rhodesia</span><span>02</span></li>
      <li><span class="sub">Childhood in Rhodesia</span><span>03</span></li>
      <li><span class="sub">Elena meets Papa</span><span>06</span></li>
    </ul>
    <svg style="position:absolute;top:380px;left:170px" width="320" height="20" viewBox="0 0 320 20"><path d="M0 16 Q160 2 320 8" stroke="var(--pink)" stroke-width="1.5" fill="none"/></svg>
  </div>
  <div class="spread-page right poem-page">
    <div class="poem">
      <p>A colleague of Elena at Harbourview School, Clara Whitlow, wrote this poem found among Elena's keepsakes</p>
      <p>To Elena</p>
      <p>Who brings small gifts<br>of mandarins from her garden</p>
      <p>left upon my desk<br>on an ordinary morning</p>
      <p>Who smiles, delighted<br>when I notice</p>
      <p>Who seems to know<br>how bright skins and green leaves<br>speak of patient care<br>and quiet kindness</p>
      <p>To Elena</p>
      <p>Who lifts a whole day<br>with a few warm words</p>
      <p>their meaning<br>a gift</p>
    </div>
    <svg class="poem-wave" width="550" height="260" viewBox="0 0 550 260">
      <path d="M0 60 Q160 150 330 70 T550 20 V260 H0Z" fill="#fff"/>
      <path d="M60 120 Q200 170 340 90 T550 40 V260 H110 Q70 190 60 120Z" fill="#b68a62"/>
    </svg>
    <div class="photo" role="img" aria-label="Photo of mandarins in a blue bowl on a wooden table" style="left:200px;bottom:40px;width:230px;height:130px;border-radius:50%;background:radial-gradient(circle,#f08a2a 35%,#5bb7c9 60%,transparent 70%)"></div>
  </div>
</section>

<!-- Celebration spread -->
<section class="spread" style="top:1870px">
  <svg class="celebration-band" viewBox="0 0 1100 96" style="z-index:2">
    <path d="M0 28 L1100 0 V72 L0 96Z" fill="var(--band)"/>
    <path d="M0 22 L1100 -6" stroke="var(--pink)" stroke-width="4"/>
  </svg>
  <div class="celebration-title" style="z-index:3">A Celebration of <span class="script">Nana Wren's</span> Life</div>
  <div class="spread-page left">
    <h3 class="section-head" style="top:220px;left:60px">Parents to Rhodesia</h3>
    <div class="body-copy" style="top:265px;left:60px;width:200px">
      <p>Born in Goa, Elena's father, Tomas Aurelio, was looking for a better life, with opportunities to bring up a family in a better environment.</p>
      <p>He took a boat with some mates to East Africa travelling inland from Beira to Salisbury, Southern Rhodesia and found a land of opportunity with space, good soil</p>
    </div>
    <div class="body-copy" style="top:265px;left:285px;width:215px">
      <p>and magnificent weather. Tomas was offered work as an apprentice dressmaker. He returned to Goa, married Rosa Celeste and took her on a wild adventure across the Indian Ocean to make a new life, along with their four poster bed. Tomas was a skilled tailor and quickly established a business along with the other new immigrant Goan families.</p>
    </div>
    <div class="photo-band">
      <div class="photo" role="img" aria-label="Black and white family group photo outside a house" style="left:40px;top:25px;width:220px;height:205px;background:linear-gradient(160deg,#9a9a9a,#4a4a4a)"></div>
      <div class="photo" role="img" aria-label="Colour family photo in a garden" style="left:280px;top:25px;width:230px;height:205px;background:linear-gradient(160deg,#8a6a3a,#5f7a42 55%,#a84a3a)"></div>
    </div>
    <div class="band-line" style="top:735px"></div>
  </div>
  <div class="spread-page right">
    <h3 class="section-head" style="top:220px;left:40px">Childhood in Rhodesia</h3>
    <div class="body-copy" style="top:265px;left:40px;width:230px">
      <p>Elena's parents built a home in Avondale which was renowned for hospitality, sharing all that they had with friends and neighbours.</p>
      <p>Rosa Celeste devoted the next 20 years welcoming eight little Pereira babies: Paulo, Felix, Amara, Hugo, Nuno, Afonso, Rui and the last little rascal named Elena.</p>
    </div>
    <div class="photo-band">
      <div class="photo" role="img" aria-label="Black and white portrait of young Elena" style="left:30px;top:25px;width:150px;height:205px;background:linear-gradient(160deg,#b5b5b5,#555)"></div>
      <div class="photo" role="img" aria-label="Black and white photo of a large family gathering" style="left:195px;top:25px;width:325px;height:205px;background:linear-gradient(160deg,#a5a5a5,#3f3f3f)"></div>
    </div>
    <div class="band-line" style="top:735px"></div>
  </div>
</section>

<!-- Memories spread -->
<section class="spread" style="top:2820px">
  <div class="spread-page left dark-page">
    <div class="body-copy" style="top:50px;left:45px;width:250px">
      <p>The home was a frenzy of activity with many visitors mostly from Mozambique who came to Salisbury for medical treatment. In return the family enjoyed many memorable holidays by the beaches and restaurants of Mozambique. Very sadly Elena's dad passed away when she was only nine. Elena was essentially brought up by her six brothers and a sister which was a mixed blessing as she was teased mercilessly but spoiled outrageously. She loved them all so much. Her mother was gentle, hardworking, selfless and an astonishingly good cook. Elena was her assistant from when she could reach the bench to when she got married.</p>
    </div>
    <div class="photo" role="img" aria-label="Black and white photo of a man holding two small children beside a life ring" style="left:315px;top:40px;width:200px;height:250px;background:linear-gradient(160deg,#cfcfcf,#5a5a5a)"></div>
    <div class="photo" role="img" aria-label="Colour photo of family and friends gathered around a long party table" style="left:40px;top:330px;width:475px;height:360px;background:linear-gradient(170deg,#d8c7a5,#7c6a55 45%,#3b5a3a 80%,#c9b7a0)"></div>
    <div class="band-line" style="top:725px"></div>
  </div>
  <div class="spread-page right">
    <div class="photo" role="img" aria-label="Black and white photo of young Elena smelling a flower" style="left:40px;top:30px;width:240px;height:200px;background:linear-gradient(90deg,#444,#bbb 60%,transparent)"></div>
    <div class="band-line" style="top:240px;left:40px;right:40px;height:3px"></div>
    <div class="photo" role="img" aria-label="Colour photo of Elena as a child with a birthday cake" style="left:60px;top:260px;width:200px;height:175px;background:linear-gradient(160deg,#6d8a52,#d99aa8 60%,#5a4a42)"></div>
    <div class="photo" role="img" aria-label="Colour photo of a family party with balloons" style="left:60px;top:450px;width:200px;height:175px;background:linear-gradient(160deg,#d8a35a,#a5503f 60%,#3f302a)"></div>
    <div class="body-copy" style="top:265px;left:290px;width:220px">
      <p>The Pereira family were involved in many multicultural events taking every opportunity to make people feel included. Although the country was divided by race the family lived life to the fullest and created their own opportunities.</p>
      <p>Elena made the most of her time at school and shone above the other students purely because she just loved to learn new things. She was well liked with many friends as she was humble, hard working and caring. She also had a twinkle in her eye with a huge smile. It is hard to find a photo where she does not radiate happiness.</p>
    </div>
  </div>
</section>

</body>
</html>
```